Portal Panel Medic need professional looking business card printed on plastic, Commericial, Industri

We are family owned and operated garage door company in Indianapolis, Indiana. We sale service and install dock equipment, doors, operators. We are looking to expand our commercial/ industrial division. We also service all residential doors and operators. We are looking for a business that stands out of the crowd. We are committed to have the best customer service in the industry.

Target Market(s)

National and local general contractors, National/ Corpate service accounts,

Industry/Entity Type

Business Service

Contact Information for Business Card

To be printed on plastic stock

Font styles to use
Sans Serif

Colors
ffffff
f04a50
ec1f27

Requirements
Must have
• Name, website,email, phone number, position.
Nice to have
• A standout professional design

```html
<!DOCTYPE html>
<html lang="en">
<head>
<meta charset="utf-8">
<title>Portal Panel Medic — Business Card</title>
<link rel="stylesheet" href="https://fonts.googleapis.com/css2?family=Roboto:wght@400;500&display=swap">
<style>
  :root {
    --page-bg: #e9e6e2;
    --card-top: #e3e6e8;
    --card-bottom: #cfd4d7;
    --card-edge: #f5f7f8;
    --red-light: #f04a50;
    --red-deep: #ec1f27;
    --white: #ffffff;
    --ink-dark: #1c1c1e;
  }
  * { box-sizing: border-box; margin: 0; padding: 0; }
  html, body {
    width: 1200px;
    height: 969px;
    overflow: hidden;
    background: var(--page-bg);
    font-family: "Roboto", Arial, sans-serif;
  }
  .card {
    position: absolute;
    left: 100px;
    top: 200px;
    width: 1000px;
    height: 570px;
    background: linear-gradient(160deg, var(--card-top), var(--card-bottom));
    border: 2px solid var(--card-edge);
    border-radius: 4px;
    box-shadow: 0 18px 40px rgba(0,0,0,0.12);
    overflow: hidden;
  }
  .contact-panel {
    position: absolute;
    left: 0;
    top: 152px;
    width: 381px;
    height: 262px;
    background: linear-gradient(135deg, var(--red-deep), var(--red-light));
    color: var(--white);
    padding: 42px 0 0 48px;
  }
  .contact-name {
    font-size: 31px;
    font-weight: 500;
    letter-spacing: 0.5px;
    line-height: 1;
  }
  .contact-role {
    margin-top: 14px;
    font-size: 23px;
    font-weight: 400;
    line-height: 1;
  }
  .contact-list {
    list-style: none;
    margin-top: 26px;
  }
  .contact-item {
    display: flex;
    align-items: center;
    gap: 14px;
    font-size: 22px;
    line-height: 31px;
    opacity: 0.95;
  }
  .contact-icon {
    width: 18px;
    height: 18px;
    flex: none;
    fill: var(--white);
  }
  .brand-name {
    position: absolute;
    left: 580px;
    top: 262px;
    font-size: 36px;
    font-weight: 500;
    line-height: 1;
    color: var(--ink-dark);
    white-space: nowrap;
  }
  .edge-bar {
    position: absolute;
    right: 0;
    top: 152px;
    width: 22px;
    height: 262px;
    background: var(--ink-dark);
  }
</style>
</head>
<body>
  <main class="card">
    <section class="contact-panel">
      <h1 class="contact-name">EVAN MARLOW</h1>
      <p class="contact-role">CEO/FOUNDER</p>
      <ul class="contact-list">
        <li class="contact-item">
          <svg class="contact-icon" viewBox="0 0 24 24" aria-hidden="true"><path d="M6.6 10.8a15.1 15.1 0 0 0 6.6 6.6l2.2-2.2a1 1 0 0 1 1-.25 11.4 11.4 0 0 0 3.6.57 1 1 0 0 1 1 1V20a1 1 0 0 1-1 1A17 17 0 0 1 3 4a1 1 0 0 1 1-1h3.5a1 1 0 0 1 1 1c0 1.25.2 2.45.57 3.57a1 1 0 0 1-.25 1z"/></svg>
          <span>555 014 2290</span>
        </li>
        <li class="contact-item">
          <svg class="contact-icon" viewBox="0 0 24 24" aria-hidden="true"><path d="M2 5h20v14H2z M3.5 6.5v.4L12 12.5l8.5-5.6v-.4z" fill-rule="evenodd"/></svg>
          <span>office@panelmedic.com</span>
        </li>
        <li class="contact-item">
          <svg class="contact-icon" viewBox="0 0 24 24" aria-hidden="true"><path d="M12 2a10 10 0 1 0 0 20 10 10 0 0 0 0-20zm-1 17.9A8 8 0 0 1 4.1 10.6L9 15.5v1a2 2 0 0 0 2 2zm6.9-2.5A2 2 0 0 0 16 16h-1v-3a1 1 0 0 0-1-1H8v-2h2a1 1 0 0 0 1-1V7h2a2 2 0 0 0 2-2v-.4a8 8 0 0 1 2.9 12.8z"/></svg>
          <span>www.panelmedic.com</span>
        </li>
      </ul>
    </section>

    <p class="brand-name">Portal Panel Medic</p>

    <span class="edge-bar" aria-hidden="true"></span>
  </main>
</body>
</html>
```